Altamira Business Card Design

The name of the business is Ruben Altamira, CPA LLC
The service that we offer is Accounting, Tax & Consulting Services. I need it to have the following items:
Ruben Altamira, Principal
Phone Number
Email Address
Physical Address

I have attached the company logo, one in black and one in white. Please provide a design in black background and the other in white background. Please include "Accounting, Tax & Consulting Services". I want the business card to be clean and very professional.

```html
<!DOCTYPE html>
<html lang="en">
<head>
<meta charset="utf-8">
<title>Ruben Altamira, CPA LLC — Business Card</title>
<link href="https://fonts.googleapis.com/css2?family=Arimo:ital,wght@0,400;0,700;1,400&family=Montserrat:wght@600&display=swap" rel="stylesheet">
<style>
  :root {
    --stage: #1c1c1d;
    --card: #353536;
    --card-pattern-a: #2f2f30;
    --card-pattern-b: #3a3a3b;
    --red: #a31b1f;
    --white: #ffffff;
    --muted: #bdbdbd;
  }
  * { box-sizing: border-box; margin: 0; padding: 0; }
  html, body { width: 1200px; height: 900px; overflow: hidden; }
  body {
    background: var(--stage);
    font-family: "Arimo", Arial, sans-serif;
    color: var(--white);
    position: relative;
  }
  .card {
    position: absolute;
    left: 330px;
    width: 540px;
    height: 309px;
    border-radius: 22px;
    background: var(--card);
    overflow: hidden;
  }
  .card--front { top: 110px; }
  .card--back { top: 470px; }

  /* Front */
  .front__accent {
    position: absolute;
    left: 0; top: 38px;
    width: 26px; height: 34px;
    background: var(--red);
  }
  .front__name {
    position: absolute;
    left: 40px; top: 38px;
    font-size: 30px;
    font-weight: 400;
    letter-spacing: 0.5px;
    color: var(--red);
    text-transform: uppercase;
    line-height: 1;
  }
  .front__title {
    position: absolute;
    left: 26px; top: 76px;
    font-size: 15px;
    font-style: italic;
    color: var(--white);
  }
  .brand {
    position: absolute;
    display: flex;
    align-items: center;
    gap: 10px;
    font-family: "Montserrat", Arial, sans-serif;
    font-weight: 600;
    font-size: 17px;
    letter-spacing: 0.5px;
    color: var(--white);
    text-transform: uppercase;
    white-space: nowrap;
  }
  .brand__square {
    width: 14px; height: 14px;
    background: var(--red);
    flex: none;
  }
  .front__brand { right: 28px; top: 138px; }
  .contact {
    position: absolute;
    right: 28px; top: 186px;
    list-style: none;
    font-size: 15px;
    line-height: 21px;
    text-align: left;
    width: 300px;
  }
  .contact__item {
    display: flex;
    align-items: center;
    gap: 8px;
  }
  .contact__item--plain { padding-left: 20px; }
  .contact__icon { width: 12px; height: 12px; flex: none; }

  /* Back */
  .back__pattern {
    position: absolute;
    inset: 0;
    background: linear-gradient(135deg, var(--card-pattern-a) 0%, var(--card-pattern-b) 55%, var(--card-pattern-a) 100%);
  }
  .back__tagline {
    position: absolute;
    right: 150px; bottom: 70px;
    font-size: 16px;
    font-style: italic;
    color: var(--white);
  }
  .back__brand {
    position: absolute;
    right: 28px; bottom: 48px;
    font-family: "Montserrat", Arial, sans-serif;
    font-weight: 600;
    font-size: 13px;
    line-height: 1.25;
    color: var(--white);
    text-transform: uppercase;
    display: flex;
    align-items: center;
    gap: 8px;
    width: 110px;
  }
</style>
</head>
<body>

  <section class="card card--front" aria-label="Business card front">
    <div class="front__accent"></div>
    <h1 class="front__name">Ruben Altamira</h1>
    <p class="front__title">Principal</p>

    <div class="brand front__brand">
      <span class="brand__square"></span>
      <span>Ruben Altamira, CPA LLC</span>
    </div>

    <ul class="contact">
      <li class="contact__item contact__item--plain">1480 N Castillo Avenue</li>
      <li class="contact__item contact__item--plain">Verano County 6042</li>
      <li class="contact__item">
        <svg class="contact__icon" viewBox="0 0 12 12" aria-hidden="true"><path fill="#a31b1f" d="M2.4 0.6l2 2-1 1.3c.7 1.5 2 2.8 3.6 3.6l1.3-1 2 2-1.2 1.9C5.4 10.3 1.7 6.6 0.6 1.9z"/></svg>
        215-630-2918
      </li>
      <li class="contact__item">
        <svg class="contact__icon" viewBox="0 0 12 12" aria-hidden="true"><rect x="0.5" y="2" width="11" height="8" fill="#a31b1f"/><path d="M0.5 2L6 6.5 11.5 2" stroke="#353536" fill="none"/></svg>
        info@rubenaltamiracpa.com
      </li>
      <li class="contact__item">
        <svg class="contact__icon" viewBox="0 0 12 12" aria-hidden="true"><circle cx="6" cy="6" r="5.5" fill="#a31b1f"/><path d="M0.5 6h11M6 0.5c2.2 2.5 2.2 8.5 0 11M6 0.5c-2.2 2.5-2.2 8.5 0 11" stroke="#353536" fill="none" stroke-width="0.8"/></svg>
        www.rubenaltamiracpa.com
      </li>
    </ul>
  </section>

  <section class="card card--back" aria-label="Business card back">
    <div class="back__pattern" role="img" aria-label="Embossed repeating brand pattern in dark grey tones"></div>
    <p class="back__tagline">Accounting, Tax &amp; Consulting Services</p>
    <div class="back__brand">
      <span class="brand__square"></span>
      <span>Ruben Altamira</span>
    </div>
  </section>

</body>
</html>
```